Unique Business Card Design

Unique Business Card design for our orthotic and prosthetic company. Our logo is on our website, color is light blue. Unique shape (artificial leg shaped, vertical, etc..) preferred. Logo, business name, individual name and basic demographics needed.

Industry/Entity Type

Business

Contact Information for Business Card

Logo, Industry, Phone # Logo, "Prosthetic & Orthotic Services" Place to add individual name and contact info

Colors
cee9f5

Requirements
Must have
• The icon must be there, placement of "Prosthetic & Orthotic Services" can be moved
Nice to have
• Like the mix of light blue, and a little darker blue. One design included the icons from my website which was a nice touch

```html
<!DOCTYPE html>
<html lang="en">
<head>
<meta charset="utf-8">
<title>Limbwell Inc. Business Card</title>
<link rel="stylesheet" href="https://fonts.googleapis.com/css2?family=Open+Sans:wght@600&family=Roboto:wght@400&family=Saira+Semi+Condensed:wght@600&family=Crimson+Text:ital@1&display=swap">
<style>
  :root {
    --brand-blue: #245f94;
    --brand-blue-deep: #1f5486;
    --paper: #f3f3f1;
    --ink-light: #ffffff;
    --swoosh-dark: #3a3f44;
    --stage: #e4e4e4;
  }
  * { margin: 0; padding: 0; box-sizing: border-box; }
  html, body { width: 1200px; height: 576px; overflow: hidden; background: var(--stage); }
  .canvas { position: relative; width: 1200px; height: 576px; }

  .card {
    position: absolute;
    border-radius: 6px;
    overflow: hidden;
    box-shadow: 0 3px 6px rgba(0,0,0,0.25);
  }
  .card--front {
    left: 82px; top: 139px; width: 484px; height: 293px;
    background: linear-gradient(180deg, var(--brand-blue) 0%, var(--brand-blue-deep) 100%);
    color: var(--ink-light);
  }
  .card--back {
    left: 602px; top: 138px; width: 480px; height: 291px;
    background: var(--brand-blue);
    color: var(--ink-light);
  }

  .brand-dot {
    position: absolute; border-radius: 50%;
  }
  .card--front .brand-dot { left: 91px; top: 106px; width: 78px; height: 78px; background: var(--ink-light); }
  .card--back .brand-dot { left: 344px; top: 21px; width: 72px; height: 72px; background: var(--brand-blue); }

  .brand-name {
    position: absolute;
    font-family: "Open Sans", sans-serif;
    font-weight: 600;
    white-space: nowrap;
  }
  .card--front .brand-name { left: 190px; top: 104px; font-size: 24px; color: var(--ink-light); }
  .card--back .brand-name { left: 300px; width: 160px; text-align: center; top: 102px; font-size: 17px; color: var(--brand-blue); }

  .brand-rule { position: absolute; height: 2px; }
  .card--front .brand-rule { left: 190px; top: 137px; width: 202px; background: var(--ink-light); }
  .card--back .brand-rule { left: 308px; top: 124px; width: 145px; background: var(--brand-blue); }

  .brand-tagline {
    position: absolute;
    font-family: "Crimson Text", serif;
    font-style: italic;
    white-space: nowrap;
    text-align: center;
  }
  .card--front .brand-tagline { left: 190px; width: 202px; top: 142px; font-size: 14px; }
  .card--back .brand-tagline { left: 300px; width: 160px; top: 128px; font-size: 10.5px; color: var(--brand-blue); }

  .front-phone {
    position: absolute; left: 190px; width: 202px; top: 160px;
    text-align: center;
    font-family: "Open Sans", sans-serif; font-weight: 600;
    font-size: 21px; letter-spacing: 1px;
  }

  .back-panel { position: absolute; inset: 0; }

  .person { position: absolute; left: 29px; top: 44px; }
  .person__name { font-family: "Saira Semi Condensed", sans-serif; font-weight: 600; font-size: 19px; line-height: 1.1; }
  .person__title { font-family: "Roboto", sans-serif; font-style: italic; font-size: 11px; margin-top: 2px; }
  .person__mobile { display: flex; align-items: center; gap: 10px; margin-top: 4px; font-family: "Roboto", sans-serif; font-size: 14px; }

  .contact-list {
    position: absolute; left: 29px; top: 200px; list-style: none;
    font-family: "Roboto", sans-serif; font-size: 12.5px;
  }
  .contact-list li { display: flex; align-items: center; gap: 12px; height: 17.5px; }
  .icon { width: 12px; height: 12px; fill: var(--ink-light); flex: none; }

  .address {
    position: absolute; right: 21px; top: 235px; text-align: right;
    font-family: "Roboto", sans-serif; font-size: 12.5px; line-height: 17.5px;
  }
</style>
</head>
<body>
<main class="canvas">

  <section class="card card--front">
    <span class="brand-dot"></span>
    <div class="brand-name">LIMBWELL INC.</div>
    <div class="brand-rule"></div>
    <div class="brand-tagline">Prosthetic &amp; Orthotic Services</div>
    <div class="front-phone">718.555.0190</div>
  </section>

  <section class="card card--back">
    <svg class="back-panel" width="480" height="291" viewBox="0 0 480 291" aria-hidden="true">
      <path d="M168 0 C205 20 225 95 270 150 C320 205 400 215 480 220 L480 0 Z" fill="var(--swoosh-dark)"/>
      <path d="M182 0 C218 18 238 95 282 148 C330 200 405 208 480 208 L480 0 Z" fill="var(--paper)"/>
    </svg>

    <span class="brand-dot"></span>
    <div class="brand-name">LIMBWELL INC.</div>
    <div class="brand-rule"></div>
    <div class="brand-tagline">Prosthetic &amp; Orthotic Services</div>

    <div class="person">
      <div class="person__name">Miriam Halden</div>
      <div class="person__title">Orthotist/Prosthetist</div>
      <div class="person__mobile">
        <svg class="icon" viewBox="0 0 12 12"><path d="M3 0h6a1 1 0 0 1 1 1v10a1 1 0 0 1-1 1H3a1 1 0 0 1-1-1V1a1 1 0 0 1 1-1zm0 1.5v8h6v-8zM5.5 10.2h1v1h-1z"/></svg>
        <span>845-555-0142</span>
      </div>
    </div>

    <ul class="contact-list">
      <li>
        <svg class="icon" viewBox="0 0 12 12"><path d="M1 3.5C1 2 3 1 6 1s5 1 5 2.5V5H8.5V4h-5v1H1zM3 5.5h6l2 3V11H1V8.5z"/></svg>
        <span>718.555.0190</span>
      </li>
      <li>
        <svg class="icon" viewBox="0 0 12 12"><path d="M3 0h6v3H3zM1 4h10v5H9V7H3v2H1zM3.5 8h5v4h-5z"/></svg>
        <span>718.555.0191</span>
      </li>
      <li>
        <svg class="icon" viewBox="0 0 12 12"><path d="M6 0a6 6 0 1 0 0 12A6 6 0 0 0 6 0zm0 1c.8.7 1.4 2.1 1.5 4.5h-3C4.6 3.1 5.2 1.7 6 1zM1 6.5h2.5c.1 1.8.4 3.2 1 4.2A5 5 0 0 1 1 6.5zm0-1a5 5 0 0 1 3.5-4.2c-.6 1-.9 2.4-1 4.2zm3.5 1h3c-.1 2.4-.7 3.8-1.5 4.5-.8-.7-1.4-2.1-1.5-4.5zm4 0H11a5 5 0 0 1-3.5 4.2c.6-1 .9-2.4 1-4.2zm0-1c-.1-1.8-.4-3.2-1-4.2A5 5 0 0 1 11 5.5z"/></svg>
        <span>www.limbwellinc.com</span>
      </li>
      <li>
        <svg class="icon" viewBox="0 0 12 12"><path d="M0 2.5h12v.8L6 7 0 3.3zM0 4.5l6 3.7 6-3.7V10H0z"/></svg>
        <span>mhalden@limbwellinc.com</span>
      </li>
    </ul>

    <address class="address" style="font-style: normal;">
      2260 West 14th Street<br>
      Brooklyn, NY 11230
    </address>
  </section>

</main>
</body>
</html>
```